A landing page- for our luxury toothbrush company called "Vorá"

A landing page to gain interest, traction, and potentially presales for our luxury toothbrush brand Vorá. I would like something like this -- does not have to be exact
LANDING PAGE OUTLINE
1️⃣ HERO SECTION (Above the Fold)
Headline:
Rethink Your Daily Pennet.
Subheadline:
A luxury, refillable toothbrush designed with intention — where beauty meets dentistry.
Buttons:
Join the Founding List or Email list
Link to complete survey for 20% off first purchase
Small line underneath:
Launching Fall 2026 · Limited Founder’s Edition
2️⃣ THE PROBLEM (Emotional Framing)
Headline:
Oral care hasn’t evolved like beauty has.
Copy:
We invest in skincare rituals.
We curate our bathrooms.
We obsess over packaging and detail.
Yet the toothbrush — something we use twice daily — remains clinical, disposable, and uninspired.
You deserve better.
3️⃣ THE PRODUCT (Your Differentiation)
Headline:
Designed to be Displayed. Engineered to Perform.
Bullets (Luxury + Function):
• Hand-finished premium prints on an acetate handle
• Slim sculptural silhouette
• Gold-accent detailing
• Replaceable brush head system
• Premium bristles (dentist-selected)
• Designed by a practicing dentist
- Custom engraving
4️⃣ THE REFILL MODEL
Headline:
Luxury That Lasts.
Instead of discarding your entire brush, simply replace the head every 3 months.
Cleaner. Smarter. Elevated.
Micro-copy:
Refill subscriptions available at launch.
5️⃣ SOCIAL IMPACT (Your 5% Donation Angle)
Headline:
Beauty With Purpose.
5% of profits are donated to organizations chosen by our community.
As a Founder, you help decide where we give.
6️⃣ SOCIAL PROOF (Even Pre-Launch)
You can use:
Dentist credibility statement
~not made yet- will edit in~
Example testimonial style:
“Finally, a toothbrush I don’t want to hide in a drawer.”
7️⃣ FOUNDER CTA SECTION
Headline:
Become a Founding Member.
Be the first to receive:
Early access pricing
Engraving perks
First charity vote
Follow us on:
Pictagrid
Zapclip
~ don't have these made yet, will add in later~
🎯 Design Direction
Page should feel closer to:
Brimelle
Quilo
Pennet
Not:
Dentix-Q
Minimal navigation.
Lots of white space.
Cream, bone, tortoise, gold tones.
Soft serif typography.
I have attached a picture of the clean vibe I would like- doesn't have to be exact but for inspo
I will also include/add our mock up drawings when they are finished!
Thank you :)

```html
<!DOCTYPE html>
<html lang="en">
<head>
<meta charset="utf-8">
<title>Vorá — Rethink Your Daily Pennet</title>
<link href="https://fonts.googleapis.com/css2?family=Abril+Fatface&family=Lato:ital,wght@0,400;0,700;1,400&display=swap" rel="stylesheet">
<style>
:root{
  --gold:#B8924A;
  --cream:#F5EDE3;
  --bone:#F8F3EC;
  --ink:#1B1B1B;
  --text:#3A3A3A;
  --muted:#6B6B6B;
  --brown:#4A3226;
  --footer:#1C1C1C;
  --white:#FFFFFF;
}
*{margin:0;padding:0;box-sizing:border-box}
html,body{width:1200px;height:4348px;overflow:hidden}
body{position:relative;background:var(--white);font-family:'Lato',sans-serif;color:var(--text)}
.abs{position:absolute}
.serif{font-family:'Abril Fatface',serif;font-weight:400}
.btn{position:absolute;display:flex;align-items:center;justify-content:center;background:var(--gold);color:var(--white);border-radius:22px;font-size:14px;font-family:'Lato',sans-serif}
.placeholder{position:absolute}

/* nav */
.brand-logo{font-family:'Abril Fatface',serif;color:var(--ink);line-height:1}
.nav-link{position:absolute;top:42px;font-size:14px;color:var(--text)}
.nav-link.active{color:var(--gold);border-bottom:2px solid var(--gold);padding-bottom:2px}

/* hero */
.hero-photo{left:25px;top:103px;width:1148px;height:560px;border-radius:24px;overflow:hidden;background:linear-gradient(90deg,#000 0 17%,#6d5c55 17%,#8a7a72 45%,#5a3b32 75%,#3a2520 100%)}
.hero-card{left:83px;top:164px;width:471px;height:439px;background:var(--cream);border-radius:20px;padding:40px 38px}
.hero-title{font-size:42px;line-height:1.25;color:var(--ink)}
.hero-title .accent{color:var(--gold)}
.hero-sub{font-size:22px;line-height:1.4;color:var(--text);margin-top:14px}
.hero-note{position:absolute;left:38px;top:334px;font-family:'Abril Fatface',serif;font-size:15px;line-height:1.5;color:var(--brown);text-decoration:underline}

/* problem */
.problem-photo{left:111px;top:793px;width:377px;height:338px;border-radius:16px 80px 16px 16px;background:linear-gradient(135deg,#cfd3d6,#8b8f93 55%,#2d2d2f)}
.section-title{font-size:42px;line-height:1.22;color:var(--ink)}
.bullet{position:absolute;font-size:17px;line-height:1.5;color:var(--text);padding-left:22px}
.bullet::before{content:"";position:absolute;left:0;top:8px;width:9px;height:9px;border-radius:50%;background:var(--gold)}

/* product */
.feature{position:absolute;font-size:20px;line-height:1.35;color:var(--text)}
.feature-lead{position:absolute;left:470px;top:1456px;width:260px;text-align:center;font-family:'Abril Fatface',serif;font-size:18px;line-height:1.45;color:var(--brown)}

/* refill */
.refill{left:42px;top:1831px;width:1116px;height:459px;border-radius:20px;overflow:hidden;background:linear-gradient(120deg,#5b5754,#7a6f69 45%,#4a3e3a)}
.refill-copy{position:absolute;left:0;top:134px;width:100%;text-align:center;color:var(--white)}
.refill-copy h2{font-size:42px}
.refill-copy p{font-size:22px;line-height:1.4;margin-top:14px}
.refill-copy em{display:block;font-size:18px;margin-top:12px}

/* testimonials */
.t-card{position:absolute;top:2493px;width:469px;height:269px;background:var(--white);box-shadow:0 2px 14px rgba(0,0,0,.12);padding:32px 34px}
.t-card p{font-size:15.5px;line-height:1.65;text-align:justify;color:var(--text)}
.t-avatar{position:absolute;left:34px;top:156px;width:80px;height:80px;border-radius:50%;background:radial-gradient(circle at 50% 40%,#b7a79a,#4b4f58)}
.t-name{position:absolute;left:128px;top:168px;font-size:20px;color:var(--gold)}
.t-role{position:absolute;left:128px;top:198px;font-size:15px;color:var(--text)}

/* impact */
.impact{left:0;top:2878px;width:1200px;height:451px;background:var(--cream)}

/* founding */
.founding-photo{left:711px;top:3452px;width:378px;height:338px;border-radius:16px 80px 16px 16px;background:linear-gradient(135deg,#e9dfd8,#d8b8b2 50%,#b97f86)}

/* footer */
.footer{left:0;top:3916px;width:1200px;height:432px;background:var(--footer);color:var(--white)}
.f-head{position:absolute;top:108px;font-size:20px;font-weight:700}
.f-link{position:absolute;font-size:14px}
.f-divider{position:absolute;left:0;top:380px;width:1200px;height:1px;background:#3a3a3a}
</style>
</head>
<body>

<!-- Navigation -->
<div class="abs brand-logo" style="left:132px;top:14px;font-size:84px;">Vorá</div>
<a class="nav-link active" style="left:429px;">Home</a>
<a class="nav-link" style="left:515px;">The Problem</a>
<a class="nav-link" style="left:645px;">The Brush</a>
<a class="nav-link" style="left:758px;">Refill Model</a>
<div class="btn" style="left:886px;top:30px;width:203px;height:41px;">Join the Founding List</div>

<!-- Hero -->
<div class="placeholder hero-photo" role="img" aria-label="Photo of a mother and young daughter brushing their teeth together"></div>
<div class="abs hero-card">
  <h1 class="serif hero-title"><span class="accent">Rethink</span> Your Daily Pennet.</h1>
  <p class="hero-sub">A luxury, refillable toothbrush designed with intention — where beauty meets dentistry.</p>
  <div class="btn" style="left:38px;top:266px;width:202px;height:41px;">Join the Founding List</div>
  <div class="hero-note">Launching Fall 2026 · Limited Founder’s<br>Edition</div>
</div>

<!-- The Problem -->
<div class="placeholder problem-photo" role="img" aria-label="Photo of hands holding a black electric toothbrush over a sink"></div>
<h2 class="abs serif section-title" style="left:571px;top:776px;width:540px;">Oral care hasn’t Evolved like Beauty has.</h2>
<div class="bullet" style="left:571px;top:904px;">We invest in skincare rituals.</div>
<div class="bullet" style="left:850px;top:904px;">We curate our bathrooms.</div>
<div class="bullet" style="left:571px;top:942px;width:240px;">We obsess over packaging and detail.</div>
<div class="bullet" style="left:850px;top:942px;">You deserve better.</div>
<div class="bullet" style="left:571px;top:1005px;width:520px;">Yet the toothbrush - something we use twice daily - remains clinical, disposable, and uninspired.</div>
<div class="btn" style="left:571px;top:1088px;width:202px;height:41px;">Join the Founding List</div>

<!-- The Product -->
<h2 class="abs serif section-title" style="left:200px;top:1236px;width:800px;text-align:center;">Designed to be Displayed. Engineered to Perform.</h2>

<svg class="abs" style="left:0;top:1376px;" width="1200" height="455" viewBox="0 1376 1200 455" aria-hidden="true">
  <path d="M340 1831 A262 262 0 0 1 860 1831" fill="none" stroke="#F1ECE6" stroke-width="22"/>
  <path d="M345 1831 A258 258 0 0 1 855 1831" fill="none" stroke="#B5B5B5" stroke-width="1.5" stroke-dasharray="8 7"/>
  <circle cx="600" cy="1620" r="7" fill="#B8924A"/>
  <circle cx="498" cy="1640" r="6" fill="#E3D7C6"/>
  <circle cx="702" cy="1640" r="6" fill="#E3D7C6"/>
  <circle cx="412" cy="1692" r="6" fill="#E3D7C6"/>
  <circle cx="788" cy="1692" r="6" fill="#E3D7C6"/>
  <circle cx="363" cy="1767" r="6" fill="#E3D7C6"/>
  <circle cx="837" cy="1767" r="6" fill="#E3D7C6"/>
  <g fill="none" stroke="#B8924A" stroke-width="2">
    <rect x="582" y="1396" width="36" height="34" rx="4"/>
    <path d="M588 1412 h24"/>
    <circle cx="375" cy="1502" r="20"/>
    <path d="M362 1516 L388 1488"/>
    <circle cx="830" cy="1496" r="18"/>
    <path d="M820 1512 l-6 22 l16 -8 l16 8 l-6 -22"/>
    <path d="M245 1590 v44"/>
    <ellipse cx="245" cy="1594" rx="10" ry="8"/>
    <rect x="922" y="1584" width="54" height="48" rx="4"/>
    <path d="M922 1596 h54"/>
    <rect x="118" y="1690" width="42" height="50" rx="4"/>
    <path d="M126 1704 h26 M126 1714 h26 M126 1724 h18"/>
    <circle cx="1058" cy="1713" r="22"/>
    <path d="M1046 1725 L1072 1699"/>
  </g>
</svg>

<div class="feature-lead">Hand-finished premium prints on an acetate handle</div>
<div class="feature" style="left:339px;top:1548px;">Replaceable brush<br>head system</div>
<div class="feature" style="left:690px;top:1548px;width:170px;text-align:center;">Premium bristles<br>(dentist-selected)</div>
<div class="feature" style="left:219px;top:1650px;">Slim sculptural<br>silhouette</div>
<div class="feature" style="left:779px;top:1650px;width:200px;text-align:right;">Designed by a<br>practicing dentist</div>
<div class="feature" style="left:110px;top:1754px;">Gold-accent detailing</div>
<div class="feature" style="left:889px;top:1754px;width:200px;text-align:right;">Custom engraving</div>
<div class="abs brand-logo" style="left:400px;top:1686px;width:400px;text-align:center;font-size:112px;">Vorá</div>

<!-- Refill Model -->
<div class="abs refill">
  <div class="placeholder" style="inset:0;background:linear-gradient(120deg,#5b5754,#7a6f69 45%,#4a3e3a);" role="img" aria-label="Photo of a mother helping her daughter brush her teeth"></div>
  <div class="refill-copy">
    <h2 class="serif">Luxury That Lasts.</h2>
    <p>Instead of discarding your entire brush, simply replace the head every 3 months.<br>Cleaner. Smarter. Elevated.</p>
    <em>Refill subscriptions available at launch.</em>
  </div>
</div>

<!-- Social Proof -->
<h2 class="abs serif section-title" style="left:110px;top:2392px;">A New Standard in Pennet</h2>
<div class="btn" style="left:884px;top:2405px;width:201px;height:41px;">Join the Founding List</div>

<div class="t-card" style="left:110px;">
  <p>Lorem ipsum dolor sit amet, consectetur adipiscing elit, sed do eiusmod tempor incididunt ut labore et dolore magna aliqua. Quis ipsum suspendisse gravida. Risus commodo vel facilisis.</p>
  <div class="t-avatar" role="img" aria-label="Portrait photo of the reviewer"></div>
  <div class="t-name">Mara Ellis</div>
  <div class="t-role">lorem ipsum</div>
</div>
<div class="t-card" style="left:616px;">
  <p>Lorem ipsum dolor sit amet, consectetur adipiscing elit, sed do eiusmod tempor incididunt ut labore et dolore magna aliqua. Quis ipsum suspendisse gravida. Risus commodo vel facilisis.</p>
  <div class="t-avatar" role="img" aria-label="Portrait photo of the reviewer"></div>
  <div class="t-name">Mara Ellis</div>
  <div class="t-role">lorem ipsum</div>
</div>
<div class="t-card" style="left:1122px;">
  <p>Lorem ipsum dolor sit amet, consectetur adipiscing elit, sed do eiusmod tempor incididunt ut labore et dolore magna aliqua. Quis ipsum suspendisse gravida. Risus commodo vel facilisis.</p>
  <div class="t-avatar" role="img" aria-label="Portrait photo of the reviewer"></div>
  <div class="t-name">Mara Ellis</div>
  <div class="t-role">lorem ipsum</div>
</div>

<!-- Social Impact -->
<div class="abs impact">
  <div class="placeholder" style="left:0;top:120px;width:175px;height:331px;background:linear-gradient(160deg,rgba(210,220,228,.9),rgba(40,52,70,.85));border-radius:0 40px 0 0;opacity:.55;" role="img" aria-label="Photo of two electric toothbrushes, white and navy"></div>
  <div class="placeholder" style="left:975px;top:105px;width:190px;height:346px;background:linear-gradient(200deg,rgba(28,38,60,.85),rgba(225,225,225,.9));border-radius:40px 40px 0 0;opacity:.55;" role="img" aria-label="Photo of a navy electric toothbrush beside its white charging stand"></div>
  <h2 class="abs serif" style="left:0;top:100px;width:1200px;text-align:center;font-size:42px;color:var(--ink);">Beauty with Purpose.</h2>
  <p class="abs" style="left:0;top:182px;width:1200px;text-align:center;font-size:23px;color:var(--gold);">5% of profits are donated to organizations chosen by our community.</p>
  <p class="abs" style="left:0;top:226px;width:1200px;text-align:center;font-size:18px;font-style:italic;color:var(--text);">As a Founder, you help decide where we give.</p>
  <div class="btn" style="left:499px;top:296px;width:202px;height:41px;">Join the Founding List</div>
</div>

<!-- Founding CTA -->
<h2 class="abs serif section-title" style="left:112px;top:3484px;width:420px;">Become a Founding Member.</h2>
<p class="abs" style="left:110px;top:3600px;font-size:23px;color:var(--gold);">Be the first to receive:</p>
<div class="bullet" style="left:112px;top:3652px;">Early access pricing</div>
<div class="bullet" style="left:310px;top:3652px;">Engraving perks</div>
<div class="bullet" style="left:112px;top:3689px;">First charity vote</div>
<div class="btn" style="left:113px;top:3753px;width:202px;height:41px;">Join the Founding List</div>
<div class="placeholder founding-photo" role="img" aria-label="Photo of a smiling woman brushing her teeth with a white toothbrush"></div>

<!-- Footer -->
<footer class="abs footer">
  <div class="abs brand-logo" style="left:113px;top:92px;font-size:96px;color:var(--white);">Vorá</div>
  <p class="abs" style="left:113px;top:220px;font-size:14px;">Rethink Your Daily Pennet.</p>
  <div class="abs" style="left:113px;top:264px;display:flex;align-items:center;gap:8px;font-size:14px;">
    <span style="display:inline-block;width:16px;height:16px;background:var(--gold);border-radius:3px;"></span>Pictagrid
    <span style="display:inline-block;width:16px;height:16px;border:1.5px solid var(--white);border-radius:3px;margin-left:14px;"></span>Zapclip
  </div>

  <div class="f-head" style="left:435px;">Main Links</div>
  <a class="f-link" style="left:435px;top:154px;">Home</a>
  <a class="f-link" style="left:435px;top:192px;">The Problem</a>
  <a class="f-link" style="left:435px;top:231px;">The Brush</a>
  <a class="f-link" style="left:435px;top:270px;">Refill Model</a>

  <div class="f-head" style="left:653px;">Contact Us</div>
  <svg class="abs" style="left:653px;top:146px;" width="18" height="22" viewBox="0 0 18 22" fill="none" stroke="#fff" stroke-width="1.6" aria-hidden="true"><path d="M9 21s7-7 7-12A7 7 0 0 0 2 9c0 5 7 12 7 12z"/><circle cx="9" cy="9" r="2.5"/></svg>
  <span class="f-link" style="left:692px;top:150px;">123, Vorá Lane, 12345.</span>
  <svg class="abs" style="left:653px;top:208px;" width="18" height="18" viewBox="0 0 24 24" fill="none" stroke="#fff" stroke-width="1.8" aria-hidden="true"><path d="M22 16.9v3a2 2 0 0 1-2.2 2 19.8 19.8 0 0 1-8.6-3.1 19.5 19.5 0 0 1-6-6A19.8 19.8 0 0 1 2.1 4.2 2 2 0 0 1 4.1 2h3a2 2 0 0 1 2 1.7c.1.9.4 1.9.7 2.8a2 2 0 0 1-.5 2.1L8 9.9a16 16 0 0 0 6 6l1.3-1.3a2 2 0 0 1 2.1-.4c.9.3 1.8.6 2.8.7a2 2 0 0 1 1.8 2z"/></svg>
  <span class="f-link" style="left:692px;top:210px;">+1 555 014 2290</span>
  <svg class="abs" style="left:653px;top:270px;" width="18" height="14" viewBox="0 0 20 14" fill="none" stroke="#fff" stroke-width="1.6" aria-hidden="true"><rect x="1" y="1" width="18" height="12" rx="1"/><path d="M1 1l9 7 9-7"/></svg>
  <span class="f-link" style="left:692px;top:268px;">hello@voracare.com</span>

  <div class="f-head" style="left:959px;">Other Links</div>
  <a class="f-link" style="left:959px;top:154px;">Support</a>
  <a class="f-link" style="left:959px;top:192px;">Cookies Policy</a>
  <a class="f-link" style="left:959px;top:231px;">Terms &amp; Conditions</a>
  <a class="f-link" style="left:959px;top:270px;">Privacy Policy</a>

  <div class="f-divider"></div>
  <p class="abs" style="left:0;top:398px;width:1200px;text-align:center;font-size:13px;">Copyright © 2026 Vorá. All rights reserved.</p>
</footer>

</body>
</html>
```